Sports Betting Business Consultant

After 21 years in corporate life. Will be continue as consultant/advisor in sports betting industry. Need a business card. Prefer an iphone format as layout. Elements; betting,ticket, sports types soccer, basketball, tennis etc , odds etc.

```html
<!DOCTYPE html>
<html lang="en">
<head>
<meta charset="UTF-8">
<title>Deniz Arkan – Sports Betting Business Consultant</title>
<link href="https://fonts.googleapis.com/css2?family=Cabin:wght@700&family=Oswald:wght@500&family=Open+Sans:wght@400&display=swap" rel="stylesheet">
<style>
  :root {
    --backdrop: #bdbcb8;
    --card: #ffffff;
    --ink: #111111;
    --accent: #e3161d;
    --photo-dark: #0d0d0d;
    --photo-mid: #5a5a5a;
    --photo-light: #d9d9d9;
    --photo-warm: #9a4a1c;
  }
  * { margin: 0; padding: 0; box-sizing: border-box; }
  html, body {
    width: 1200px;
    height: 900px;
    overflow: hidden;
    background: var(--backdrop);
  }
  .canvas {
    position: relative;
    width: 1200px;
    height: 900px;
  }
  .card {
    position: absolute;
    left: 350px;
    top: 40px;
    width: 500px;
    height: 820px;
    background: var(--card);
    overflow: hidden;
    box-shadow: 0 10px 30px rgba(0,0,0,0.18);
  }
  .card__header {
    position: absolute;
    left: 0;
    top: 0;
    width: 500px;
    height: 470px;
  }
  .card__identity {
    position: absolute;
    left: 70px;
    top: 450px;
    width: 360px;
  }
  .card__name {
    font-family: "Cabin", sans-serif;
    font-weight: 700;
    font-size: 50px;
    letter-spacing: 1px;
    color: var(--ink);
    line-height: 1;
    text-transform: uppercase;
  }
  .card__role {
    margin-top: 6px;
    font-family: "Oswald", sans-serif;
    font-weight: 500;
    font-size: 21px;
    letter-spacing: 0.3px;
    color: var(--ink);
    text-transform: uppercase;
    line-height: 1.1;
    padding-bottom: 6px;
    border-bottom: 3px solid var(--accent);
  }
  .card__contacts {
    position: absolute;
    left: 90px;
    top: 600px;
    list-style: none;
  }
  .contact {
    display: flex;
    align-items: center;
    gap: 26px;
    margin-bottom: 14px;
    font-family: "Open Sans", sans-serif;
    font-size: 27px;
    color: var(--ink);
  }
  .contact__icon {
    width: 36px;
    height: 36px;
    background: var(--accent);
    display: flex;
    align-items: center;
    justify-content: center;
    flex-shrink: 0;
  }
  .card__band {
    position: absolute;
    left: 0;
    width: 500px;
    background: var(--ink);
  }
  .card__band--upper { top: 705px; height: 26px; }
  .card__band--lower { top: 770px; height: 24px; }
</style>
</head>
<body>
<div class="canvas">
  <article class="card">
    <svg class="card__header" viewBox="0 0 500 470" aria-hidden="false">
      <defs>
        <linearGradient id="photoTone" x1="0" y1="0" x2="0" y2="1">
          <stop offset="0" stop-color="var(--photo-dark)"/>
          <stop offset="0.55" stop-color="var(--photo-mid)"/>
          <stop offset="1" stop-color="var(--photo-light)"/>
        </linearGradient>
        <radialGradient id="warmGlow" cx="0.32" cy="0.3" r="0.35">
          <stop offset="0" stop-color="var(--photo-warm)" stop-opacity="0.7"/>
          <stop offset="1" stop-color="var(--photo-warm)" stop-opacity="0"/>
        </radialGradient>
        <clipPath id="photoClip">
          <path d="M0,0 H500 V250 Q250,470 0,330 Z"/>
        </clipPath>
      </defs>
      <g clip-path="url(#photoClip)" role="img" aria-label="Photograph of sports balls — basketball, football, soccer ball, volleyball, tennis ball, baseball — resting on scattered playing cards">
        <rect width="500" height="470" fill="url(#photoTone)"/>
        <rect width="500" height="470" fill="url(#warmGlow)"/>
      </g>
      <path class="card__swoosh" d="M0,372 Q240,480 500,290 L500,318 Q240,500 0,384 Z" fill="var(--accent)"/>
    </svg>

    <header class="card__identity">
      <h1 class="card__name">Deniz Arkan</h1>
      <p class="card__role">Sports Betting Business Consultant</p>
    </header>

    <ul class="card__contacts">
      <li class="contact">
        <span class="contact__icon">
          <svg width="20" height="20" viewBox="0 0 24 24" aria-hidden="true">
            <path fill="#fff" d="M6.6 10.8a15.1 15.1 0 0 0 6.6 6.6l2.2-2.2a1 1 0 0 1 1-.25 11.4 11.4 0 0 0 3.6.57 1 1 0 0 1 1 1V20a1 1 0 0 1-1 1A17 17 0 0 1 3 4a1 1 0 0 1 1-1h3.5a1 1 0 0 1 1 1c0 1.25.2 2.45.57 3.57a1 1 0 0 1-.25 1z"/>
          </svg>
        </span>
        <span class="contact__text">+90 555 0142 387</span>
      </li>
      <li class="contact">
        <span class="contact__icon">
          <svg width="22" height="22" viewBox="0 0 24 24" aria-hidden="true">
            <rect x="3" y="6" width="18" height="12" fill="none" stroke="#fff" stroke-width="1.8"/>
            <path d="M3 6 L12 13 L21 6" fill="none" stroke="#fff" stroke-width="1.8"/>
          </svg>
        </span>
        <span class="contact__text">dnzarkn@mailbox.com</span>
      </li>
    </ul>

    <div class="card__band card__band--upper"></div>
    <div class="card__band card__band--lower"></div>
  </article>
</div>
</body>
</html>
```